Unique Realtor Website for real state Broker

All Real Estate websites look the same with the same boring layout and info that no one cares about. What I am looking for is a Realtor/Broker site but more focused on me and my services along with client reviews and testimonials. I am primarily a buyers Broker and a Military Specialist (KT) and that's what I want to focus on. I need a tab where I can put my listings, but I don't want listings to be the focus like most sites are. I also run a nonprofit dog rescue and I want a tab to talk about that as well. I am also looking to have a more mid-century feel to my site as mid-century architecture is my passion. I sell in both San Diego and Palm Springs. There's an artist based out of Palm Springs whom I love and I would like the feel of my site to have a similar vibe (attached are some of Pelts pieces to give you a better idea). I'm also having a cartoon drawing done of myself that I would like on the site as well (should be ready in a couple days). Want to make sure that the site is SEO focused as well. my current site is: www.torvekhomes.example for reference.

Target Market(s)

Buyers

Industry/Entity Type

Real Estate Agent

Coding

Coded - Design and coding required

Number of Pages Required

5+ page

Font styles to use
Sans Serif

Colors
fece3e
fee18a
ffffff
000000
959595

Requirements
Must have
• Must be unique, fun, buyer focused with SEO capability and strong social media base
• web site need to be designed for Word Press

```html
<!DOCTYPE html>
<html lang="en">
<head>
<meta charset="utf-8">
<title>Torvek Real Estate</title>
<link href="https://fonts.googleapis.com/css2?family=Montserrat:wght@300;400;600;700;800&family=Raleway:wght@400;500&display=swap" rel="stylesheet">
<style>
:root{
  --yellow:#fece3e;
  --yellow-soft:#fee18a;
  --white:#ffffff;
  --black:#000000;
  --grey:#959595;
  --ink:#333333;
  --band:#ebebec;
  --line:#dddddd;
}
*{box-sizing:border-box;margin:0;padding:0}
html,body{width:1200px;height:4272px;overflow:hidden;background:var(--white)}
body{position:relative;font-family:'Raleway',sans-serif;color:var(--ink)}
.abs{position:absolute}
.head-font{font-family:'Montserrat',sans-serif}
.topline{left:0;top:0;width:1200px;height:4px;background:var(--yellow)}
.logo{font-family:'Montserrat',sans-serif;font-weight:300;color:var(--yellow);line-height:1}
.logo .name{font-size:58px;letter-spacing:4px;display:block}
.logo .sub{font-size:15px;letter-spacing:14px;display:block;margin-top:4px}
.social{display:flex;gap:9px;align-items:center}
.social span{width:27px;height:27px;border-radius:50%;display:block}
.c1{background:#3b5998}.c2{background:#1da1f2}.c3{background:#e0533f}
.small{font-family:'Montserrat',sans-serif;font-size:9px;color:var(--ink)}
.nav{display:flex;font-family:'Montserrat',sans-serif;font-size:10.5px;color:var(--ink);top:84px;left:492px}
.nav a{color:inherit;text-decoration:none;padding:8px 0;margin-right:32px}
.nav a.active{background:var(--yellow);color:var(--white);padding:8px 14px}
.hero{left:0;top:124px;width:1200px;height:561px;background:linear-gradient(180deg,#2a3560 0%,#3d4a78 40%,#6a5a4a 62%,#1f2a45 80%,#2c3a5a 100%)}
.hero h1{position:absolute;top:280px;width:100%;text-align:center;font-family:'Montserrat',sans-serif;font-weight:700;font-size:46px;color:var(--white);letter-spacing:1px;text-shadow:0 2px 6px rgba(0,0,0,.5)}
.search{position:absolute;top:376px;left:273px;height:64px;display:flex;font-family:'Montserrat',sans-serif}
.search .sel{width:95px;background:#e9e9e9;display:flex;align-items:center;justify-content:center;font-size:15px;gap:8px}
.search .inp{width:435px;background:rgba(255,255,255,.85);display:flex;align-items:center;padding-left:22px;font-size:13px;color:#555}
.search .btn{width:122px;background:var(--yellow);display:flex;align-items:center;justify-content:center;font-size:18px;color:#333}
.hero-arrow{position:absolute;top:256px;width:40px;height:46px;background:var(--white);display:flex;align-items:center;justify-content:center}
.dots{position:absolute;top:505px;left:547px;display:flex;gap:15px}
.dots i{width:9px;height:9px;border-radius:50%;background:var(--white);display:block}
.dots i.on{background:transparent;border:2px solid var(--white);width:11px;height:11px;margin-top:-1px}
.sec-title{width:1200px;text-align:center;font-family:'Montserrat',sans-serif;font-weight:700;font-size:28px;color:var(--yellow)}
.rule{left:550px;width:100px;height:3px;background:#b9b9b9}
.listing{width:300px;height:348px;box-shadow:0 2px 6px rgba(0,0,0,.12)}
.listing .ph{height:271px;position:relative}
.listing .feats{position:absolute;bottom:6px;left:20px;display:flex;gap:22px;color:var(--white);font-size:12px;font-family:'Montserrat',sans-serif}
.listing .band{height:77px;background:var(--yellow);padding:14px 20px;color:var(--white)}
.listing .addr{font-size:12px;color:#4a4a4a}
.listing .price{font-family:'Montserrat',sans-serif;font-weight:700;font-size:27px;margin-top:6px}
.circ-arrow{width:44px;height:44px;border-radius:50%;background:var(--black);display:flex;align-items:center;justify-content:center}
.meet{left:0;top:1293px;width:1200px;height:497px;background:var(--yellow-soft)}
.btn-y{background:var(--yellow);color:var(--ink);font-family:'Montserrat',sans-serif;font-size:13px;display:flex;align-items:center;justify-content:center;border:1px solid #f0b922}
.para{font-size:13px;line-height:22.5px;text-align:justify;color:#444}
.rescue{left:132px;top:1857px;width:938px;height:478px;border:1px solid var(--yellow)}
.grey-band{left:0;width:1200px;background:var(--band)}
.testi{width:298px;height:340px;background:var(--white)}
.testi .q{font-family:'Montserrat',sans-serif;font-weight:800;font-size:64px;color:#e0e0e0;line-height:1}
.testi p{font-size:12px;line-height:22.5px;text-align:center;color:#555}
.testi .who{position:absolute;bottom:0;left:0;right:0;border-top:1px solid #eee;padding:8px 12px;font-size:10px;color:#555}
.testi .who b{color:var(--yellow);font-weight:500}
.avatar{width:54px;height:54px;border-radius:50%;background:linear-gradient(135deg,#b9a89a,#5c5450);border:3px solid var(--white)}
.box-arrow{width:28px;height:50px;background:var(--white);display:flex;align-items:center;justify-content:center}
.review{width:300px;height:233px;border:1px solid #d9d9d9}
.review .top{height:70px;border-bottom:1px solid #d9d9d9;position:relative}
.review .nm{position:absolute;left:70px;top:16px;font-size:10px;color:#444}
.review .stars{position:absolute;left:70px;top:32px;color:var(--yellow);font-size:12px;letter-spacing:5px}
.review .av{position:absolute;left:18px;top:14px;width:40px;height:40px;border-radius:50%;background:linear-gradient(135deg,#c8b2a2,#5e534e)}
.review h4{font-family:'Montserrat',sans-serif;font-weight:400;font-size:10.5px;margin:24px 20px 0;color:#333}
.review p{font-size:11.5px;line-height:21px;margin:12px 20px 0;color:#555}
.review .more{position:absolute;left:22px;bottom:22px;font-family:'Montserrat',sans-serif;font-size:9px;color:var(--yellow)}
.review .src{position:absolute;right:18px;bottom:20px;font-family:'Montserrat',sans-serif;font-size:9px;font-weight:700;color:#c41200}
.work{height:140px}
.foot-label{font-family:'Montserrat',sans-serif;font-size:10px;color:var(--yellow)}
.foot-text{font-size:10.5px;color:#555;line-height:24px}
.bottom-links{font-size:10px;color:#555}
</style>
</head>
<body>
<div class="abs topline"></div>

<!-- header -->
<div class="abs logo" style="left:130px;top:32px"><span class="name">TORVEK</span><span class="sub">REAL ESTATE</span></div>
<div class="abs small" style="left:668px;top:37px">FOLLOW US :</div>
<div class="abs social" style="left:736px;top:28px" aria-label="Social links"><span class="c1"></span><span class="c2"></span><span class="c3"></span></div>
<svg class="abs" style="left:876px;top:34px" width="16" height="16" viewBox="0 0 24 24"><path d="M6.6 10.8a15 15 0 0 0 6.6 6.6l2.2-2.2c.3-.3.7-.4 1-.2 1.1.4 2.3.6 3.6.6.6 0 1 .4 1 1V20c0 .6-.4 1-1 1A17 17 0 0 1 3 4c0-.6.4-1 1-1h3.5c.6 0 1 .4 1 1 0 1.3.2 2.5.6 3.6.1.3 0 .7-.2 1z" fill="#fece3e"/></svg>
<div class="abs small" style="left:896px;top:38px">: CALL US : <span style="color:var(--yellow);font-size:15px">(555).555.0142</span></div>
<nav class="abs nav"><a class="active">HOME</a><a>ABOUT US</a><a>RESCUE</a><a>BUY</a><a>TESTIMONIALS</a><a>LISTINGS</a><a>CONTACT US</a></nav>

<!-- hero -->
<section class="abs hero" role="img" aria-label="Night skyline of downtown high-rises reflected on the bay">
  <h1>REAL ESTATE BROKER</h1>
  <div class="search"><div class="sel">BUY <svg width="10" height="8" viewBox="0 0 10 8"><path d="M1 2l4 4 4-4" stroke="#333" stroke-width="1.6" fill="none"/></svg></div><div class="inp">Search by Location...</div><div class="btn">SEARCH</div></div>
  <div class="hero-arrow" style="left:0"><svg width="10" height="16"><path d="M8 1L2 8l6 7" stroke="#333" stroke-width="2" fill="none"/></svg></div>
  <div class="hero-arrow" style="right:0"><svg width="10" height="16"><path d="M2 1l6 7-6 7" stroke="#333" stroke-width="2" fill="none"/></svg></div>
  <div class="dots"><i></i><i class="on"></i><i></i><i></i><i></i></div>
</section>

<!-- featured listings -->
<h2 class="abs sec-title" style="top:746px">FEATURED LISTINGS</h2>
<div class="abs rule" style="top:812px"></div>

<article class="abs listing" style="left:132px;top:877px">
  <div class="ph" role="img" aria-label="Two-storey grey clapboard house with white trim" style="background:linear-gradient(180deg,#8fb5e0,#a9a9a9 60%,#8e8a80)"><div class="feats"><span>▬ 4</span><span>◡ 2</span><span>⌂ 1</span></div></div>
  <div class="band"><div class="addr">18420 Coral Vista Avenue, San Diego</div><div class="price">$6,295,000</div></div>
</article>
<article class="abs listing" style="left:450px;top:877px">
  <div class="ph" role="img" aria-label="Red brick colonial house with white dormers among trees" style="background:linear-gradient(180deg,#5f8a4a,#8a4a3a 55%,#6b7a4a)"><div class="feats"><span>▬ 4</span><span>◡ 2</span><span>⌂ 1</span></div></div>
  <div class="band"><div class="addr">4410 Sunmesa Way Tustin, San Diego</div><div class="price">$3,988,000</div></div>
</article>
<article class="abs listing" style="left:769px;top:877px">
  <div class="ph" role="img" aria-label="Modern white villa with pool under blue sky" style="background:linear-gradient(180deg,#3f6fb0,#dcd6c8 50%,#7a9aaa)"><div class="feats"><span>▬ 4</span><span>◡ 2</span><span>⌂ 1</span></div></div>
  <div class="band"><div class="addr">31608 Ridgeline Drive, San Juan Capistrano</div><div class="price">$3,699,800</div></div>
</article>
<div class="abs circ-arrow" style="left:109px;top:1029px"><svg width="12" height="16"><path d="M9 2L3 8l6 6" stroke="#fff" stroke-width="2.5" fill="none"/></svg></div>
<div class="abs circ-arrow" style="left:1048px;top:1029px"><svg width="12" height="16"><path d="M3 2l6 6-6 6" stroke="#fff" stroke-width="2.5" fill="none"/></svg></div>

<!-- meet -->
<section class="abs meet">
  <div class="abs" role="img" aria-label="Portrait of the broker, smiling, with long platinum hair" style="left:35px;top:35px;width:640px;height:462px;background:radial-gradient(ellipse at 45% 40%,#f1d9c2 0%,#e8dcc0 30%,#3a3a3a 70%,#2a2a2a 100%)"></div>
  <div class="abs head-font" style="left:682px;top:52px;font-size:50px;font-weight:800;color:var(--white)">MEET</div>
  <div class="abs head-font" style="left:682px;top:112px;font-size:37px;font-weight:400;color:#333">DELPHINE</div>
  <p class="abs para" style="left:683px;top:188px;width:388px">For as long as I can remember, I have always had a deep love and admiration for our Armed Forces. The fact that these brave men and women, volunteer to put their lives on the line to protect our freedom is just astounding to me. I knew that when I became a Realtor, I wanted to go back to the Military so I decided to dedicate a large portion of my career to serving those who have served.</p>
  <div class="abs btn-y" style="left:684px;top:382px;width:128px;height:47px">READ MORE</div>
</section>

<!-- rescue -->
<section class="abs rescue">
  <div class="abs" style="left:45px;top:40px;font-size:38px;font-weight:400;color:#333;font-family:'Raleway',sans-serif">RESCUE</div>
  <div class="abs" style="left:46px;top:110px;font-size:13px;color:#333">Co-Founder of The Paw Haven</div>
  <div class="abs" style="left:46px;top:135px;width:362px;height:1px;background:var(--yellow)"></div>
  <p class="abs para" style="left:46px;top:156px;width:362px">Since childhood, my number one passion has been animal advocacy (In case you were wondering, yes, I was that girl who protested the frog dissection in Biology class). When I co-founded The Paw Haven in 2010, my dream of saving dogs in need was finally realized. We have saved hundreds of dogs and we focus on rescuing from high kill shelters in Southern California and from the streets of Mexico. We are a 501c Non Profit organization and we are 100% donation and volunteer run.</p>
  <div class="abs btn-y" style="left:48px;top:385px;width:127px;height:44px">READ MORE</div>
  <div class="abs" role="img" aria-label="Small rescued dog in a red sweater standing on pavement" style="left:467px;top:0;width:469px;height:476px;background:linear-gradient(160deg,#8a8784,#6f6c6a 45%,#5a4a40 70%,#8c8a88)"></div>
</section>

<!-- testimonials -->
<section class="abs grey-band" style="top:2402px;height:606px">
  <h2 class="abs sec-title" style="top:56px">TESTIMONIALS</h2>
  <div class="abs rule" style="top:118px"></div>
  <div class="abs box-arrow" style="left:105px;top:338px"><svg width="8" height="14"><path d="M7 1L1 7l6 6" stroke="#555" stroke-width="1.5" fill="none"/></svg></div>
  <div class="abs box-arrow" style="left:1068px;top:338px"><svg width="8" height="14"><path d="M1 1l6 6-6 6" stroke="#555" stroke-width="1.5" fill="none"/></svg></div>

  <article class="abs testi" style="left:132px;top:206px">
    <div class="abs q" style="left:42px;top:60px">&ldquo;</div>
    <p class="abs" style="left:38px;top:110px;width:222px">There are many variations of passages of Lorem Ipsum available, but the majority have suffered alteration in some form, by injected humour, or randomised words which don't look even slightly believable.</p>
    <div class="abs q" style="left:195px;top:222px">&rdquo;</div>
    <div class="who"><b>MARCO DELANEY,</b> Australia</div>
  </article>
  <article class="abs testi" style="left:451px;top:206px">
    <div class="abs q" style="left:42px;top:60px">&ldquo;</div>
    <p class="abs" style="left:38px;top:110px;width:222px">It is a long established fact that a reader will be distracted by the readable content of a page when looking at its layout. The point of using Lorem Ipsum is that it has a more-or-less normal .</p>
    <div class="abs q" style="left:218px;top:222px">&rdquo;</div>
    <div class="who"><b>OSKAR,</b> Australia</div>
  </article>
  <article class="abs testi" style="left:770px;top:206px">
    <div class="abs q" style="left:42px;top:60px">&ldquo;</div>
    <p class="abs" style="left:38px;top:110px;width:222px">There are many variations of passages of Lorem Ipsum available, but the majority have suffered alteration in some form, by injected humour, or randomised words which don't look</p>
    <div class="abs q" style="left:225px;top:200px">&rdquo;</div>
    <div class="who"><b>JULIAN,</b> Australia</div>
  </article>
  <div class="abs avatar" role="img" aria-label="Client portrait" style="left:132px;top:176px"></div>
  <div class="abs avatar" role="img" aria-label="Client portrait" style="left:451px;top:176px"></div>
  <div class="abs avatar" role="img" aria-label="Client portrait" style="left:770px;top:176px"></div>
</section>

<!-- client reviews -->
<h2 class="abs sec-title" style="top:3074px">CLIENT REVIEWS</h2>
<div class="abs rule" style="top:3138px"></div>
<div class="abs head-font" style="left:952px;top:3155px;width:116px;height:27px;background:var(--yellow);color:#8a6a00;font-size:9.5px;font-weight:600;display:flex;align-items:center;justify-content:center">VIEW ALL REVIEWS</div>

<article class="abs review" style="left:132px;top:3200px">
  <div class="top"><div class="av" role="img" aria-label="Reviewer portrait"></div><div class="nm">Rena T.</div><div class="stars">★★★★☆</div></div>
  <h4>EXCELLENT</h4>
  <p>My husband and I are so very thankful and blessed to have had Delphine as our realtor when we sold our home in</p>
  <div class="more">READ MORE</div><div class="src">revu</div>
</article>
<article class="abs review" style="left:452px;top:3200px">
  <div class="top"><div class="av" role="img" aria-label="Reviewer portrait"></div><div class="nm">Nora K</div><div class="stars">★★★★☆</div></div>
  <h4>GOOD</h4>
  <p>I had the privilege of working with Delphine on the purchase of our home recently.She was amazing! She was smart...</p>
  <div class="more">READ MORE</div><div class="src">revu</div>
</article>
<article class="abs review" style="left:769px;top:3200px">
  <div class="top"><div class="av" role="img" aria-label="Reviewer portrait"></div><div class="nm">Talia M</div><div class="stars">★★★★☆</div></div>
  <h4>QAULITY SERVICES</h4>
  <p>When my partner and I began our house hunt we originally used a different agent. We quickly dropped them when they ignored...</p>
  <div class="more">READ MORE</div><div class="src">revu</div>
</article>

<!-- our work -->
<section class="abs grey-band" style="top:3508px;height:382px">
  <h2 class="abs sec-title" style="top:56px">OUR WORK</h2>
  <div class="abs rule" style="top:122px"></div>
  <svg class="abs" style="left:86px;top:227px" width="14" height="24"><path d="M12 2L2 12l10 10" stroke="#777" stroke-width="2" fill="none"/></svg>
  <svg class="abs" style="left:1094px;top:227px" width="14" height="24"><path d="M2 2l10 10-10 10" stroke="#777" stroke-width="2" fill="none"/></svg>
  <div class="abs work" role="img" aria-label="Mid-century illustration of a desert party scene in olive and teal" style="left:132px;top:180px;width:249px;height:124px;background:linear-gradient(135deg,#8fa37a,#5f7e66 60%,#3b4a3a)"></div>
  <div class="abs work" role="img" aria-label="Mid-century illustration of a pink poolside garden" style="left:388px;top:180px;width:237px;height:133px;background:linear-gradient(135deg,#e58aa0,#f0b6b0 50%,#7ab090)"></div>
  <div class="abs work" role="img" aria-label="Mid-century illustration of a violet lounge with figures" style="left:632px;top:180px;width:263px;height:117px;background:linear-gradient(135deg,#8e6cc0,#6e5aa8 50%,#c0a8d8)"></div>
  <div class="abs work" role="img" aria-label="Mid-century illustration of an orange living room with fireplace" style="left:903px;top:180px;width:165px;height:138px;background:linear-gradient(135deg,#e8873a,#f2a860 55%,#c75a2a)"></div>
</section>

<!-- footer -->
<div class="abs logo" style="left:130px;top:3950px"><span class="name">TORVEK</span><span class="sub">REAL ESTATE</span></div>
<div class="abs foot-label" style="left:165px;top:4092px">FOLLOW US :</div>
<div class="abs social" style="left:254px;top:4083px" aria-label="Social links"><span class="c1"></span><span class="c2"></span><span class="c3"></span></div>

<div class="abs foot-label" style="left:472px;top:3952px">CONTACT US</div>
<svg class="abs" style="left:472px;top:4003px" width="12" height="16" viewBox="0 0 12 16"><path d="M6 0a6 6 0 0 0-6 6c0 4.5 6 10 6 10s6-5.5 6-10a6 6 0 0 0-6-6zm0 8.2A2.2 2.2 0 1 1 6 3.8a2.2 2.2 0 0 1 0 4.4z" fill="#fece3e"/></svg>
<div class="abs foot-text" style="left:503px;top:3996px">318 Harbor Lane<br>San Diego, Ca 92101</div>
<svg class="abs" style="left:472px;top:4068px" width="13" height="13" viewBox="0 0 24 24"><path d="M6.6 10.8a15 15 0 0 0 6.6 6.6l2.2-2.2c.3-.3.7-.4 1-.2 1.1.4 2.3.6 3.6.6.6 0 1 .4 1 1V20c0 .6-.4 1-1 1A17 17 0 0 1 3 4c0-.6.4-1 1-1h3.5c.6 0 1 .4 1 1 0 1.3.2 2.5.6 3.6.1.3 0 .7-.2 1z" fill="#fece3e"/></svg>
<div class="abs foot-text" style="left:503px;top:4062px">555-014-2290</div>
<svg class="abs" style="left:472px;top:4106px" width="13" height="10" viewBox="0 0 13 10"><rect width="13" height="10" fill="#fece3e"/><path d="M0 0l6.5 5L13 0" stroke="#fff" fill="none"/></svg>
<div class="abs foot-text" style="left:503px;top:4098px">hello@torvekhomes.example</div>

<div class="abs foot-label" style="left:716px;top:3952px">ASSOCIATIONS</div>
<div class="abs" role="img" aria-label="Professional association certification badge" style="left:716px;top:3990px;width:152px;height:52px;background:#e4e8f0"></div>
<div class="abs" style="left:888px;top:3990px;width:1px;height:56px;background:#999"></div>
<div class="abs" role="img" aria-label="Military relocation professional badge" style="left:905px;top:3994px;width:163px;height:46px;background:#d8dde8"></div>

<div class="abs" style="left:0;top:4182px;width:1200px;height:1px;background:var(--line)"></div>
<div class="abs bottom-links" style="left:132px;top:4212px">Home &nbsp;| &nbsp;About us &nbsp;| &nbsp;Rescue &nbsp;| &nbsp;Buy &nbsp;| &nbsp;Testimonials &nbsp;| &nbsp;Blog &nbsp;| &nbsp;Contact us</div>
<div class="abs bottom-links" style="left:884px;top:4212px">Copyrights @ 2017 All Rights Reserved</div>
<div class="abs" style="left:0;top:4262px;width:1200px;height:10px;background:var(--yellow)"></div>
</body>
</html>
```